Vandrimoss - new homepage

We need a new website design for an easy-to-use purchase order software (SAAS-system) called Vandrimoss.
We deliver an easy-to-use purchase order software that is quick to implement and provides instant values such as improved procurement efficency, better cost control and streamlined AP processing.
Users avoid manual processes and budget overspending with an easy-to-use tool. We mainly target SMEs, where a large portion of our clients are project-based businesses.
The final design should communicate a modern, easy-to-use system that provides real-time financial control, safety, great support and scalability.
Sick
Been away for another week so not fully updated. Also, feel that desings need some more polishing before happy with them. Will provide feedback and present final versions to management team next week.
1 page

```html
<!DOCTYPE html>
<html lang="en">
<head>
<meta charset="utf-8">
<title>Vandrimoss — Making cost control easy</title>
<link href="https://fonts.googleapis.com/css2?family=Poppins:ital,wght@0,400;0,500;0,600;1,400;1,500&display=swap" rel="stylesheet">
<style>
:root{
  --bg:#0c0a1c;
  --ink:#ffffff;
  --muted:#c9c5d8;
  --line:#d9d6e6;
  --orange:#ff7a12;
  --purple:#7a0fd6;
  --blue:#3d2cff;
  --tick:#27c46b;
}
*{box-sizing:border-box;margin:0;padding:0}
html,body{width:1200px;height:5133px;overflow:hidden}
body{
  position:relative;
  font-family:"Poppins",sans-serif;color:var(--ink);
  background:
    radial-gradient(ellipse 600px 500px at 600px 350px,rgba(90,30,150,.45),transparent 70%),
    radial-gradient(ellipse 700px 600px at 1150px 1700px,rgba(110,20,170,.5),transparent 70%),
    radial-gradient(ellipse 900px 700px at 700px 3000px,rgba(110,20,170,.55),transparent 70%),
    radial-gradient(ellipse 600px 500px at 1100px 2300px,rgba(90,20,150,.4),transparent 70%),
    var(--bg);
}
.abs{position:absolute}
.btn{position:absolute;display:flex;align-items:center;justify-content:center;gap:8px;border-radius:22px;font-size:12px;font-weight:500;color:#fff}
.btn-orange{background:var(--orange)}
.btn-outline{border:1.5px solid var(--line)}
.circle-arrow{width:13px;height:13px;border:1.5px solid currentColor;border-radius:50%;display:inline-flex;align-items:center;justify-content:center;font-size:8px}
.center{text-align:center;left:0;width:1200px}

.brand{display:flex;align-items:center;gap:10px;font-weight:600;font-size:30px;letter-spacing:-.5px}
.brand-mark{width:34px;height:34px;border:3px solid #fff;border-radius:50%}
.nav-links{left:604px;top:42px;display:flex;gap:34px;font-size:12px;font-weight:500}
.flag{left:968px;top:40px;width:22px;height:14px;background:#1b3b8f;border-radius:2px}
.nav-cta{left:1032px;top:34px;width:102px;height:34px;background:var(--blue);font-weight:600}

.hero-title{top:212px;font-size:56px;font-weight:500;letter-spacing:-.5px}
.hero-sub{top:304px;font-size:13px;line-height:20px;left:340px;width:520px}
.hero-note{left:426px;top:428px;font-size:8px;color:var(--muted)}
.hero-visual{left:350px;top:470px;width:520px;height:305px;border-radius:14px;
  background:linear-gradient(135deg,#d9dbe6 0%,#8b8fa8 45%,#2a2740 100%);opacity:.85}

.h2{font-size:28px;font-weight:500}

.feature{width:254px;height:254px;border:1.5px solid var(--line);border-radius:14px;padding:16px 16px}
.feature .icon{width:64px;height:64px;border:1.5px solid var(--line);border-radius:10px;display:flex;align-items:center;justify-content:center}
.feature h3{font-size:19px;font-weight:500;margin:16px 0 10px}
.feature p{font-size:11px;line-height:20px;color:var(--muted)}
.feature .more{position:absolute;left:16px;top:218px;font-size:11px}

.int-title{left:156px;top:1424px;font-size:28px;line-height:30px;font-weight:500;width:460px}
.int-text{left:156px;top:1502px;width:400px;font-size:12px;line-height:19px;color:var(--muted)}
.int-visual{left:700px;top:1370px;width:360px;height:350px;border-radius:24px;
  background:radial-gradient(ellipse 70% 70% at 65% 55%,#5b58d8 0%,#2e2a6a 45%,rgba(20,16,45,0) 80%)}

.eyebrow{font-size:11px;letter-spacing:2px}
.step{width:272px;height:272px;border-radius:50%;background:radial-gradient(circle at 50% 40%,#2a2838,#1b1a28);text-align:center;padding-top:62px}
.step .badge{width:80px;height:80px;margin:0 auto;border-radius:50%;background:#fff;display:flex;align-items:center;justify-content:center}
.step h4{font-size:14px;font-weight:600;margin:20px 0 10px}
.step p{font-size:10px;line-height:17px;color:var(--muted);width:200px;margin:0 auto}

.plan{width:254px;height:526px;border:1.5px solid var(--line);border-radius:14px;padding:30px 34px}
.plan.gold{background:var(--purple);border-color:var(--purple)}
.plan .name{font-size:15px;font-weight:500}
.plan .price{font-size:21px;font-weight:600;margin-top:14px}
.plan .price small{font-size:14px}
.plan .trial{font-size:12px;font-style:italic;color:var(--muted);margin-top:4px}
.plan ul{list-style:none;margin-top:30px}
.plan li{display:flex;align-items:center;gap:12px;font-size:12px;height:28.5px;color:var(--muted)}
.plan li::before{content:"";width:12px;height:12px;border:1.5px solid var(--tick);border-radius:50%;
  background:radial-gradient(circle,var(--tick) 2px,transparent 2.5px)}
.plan.gold li{color:#f1e6ff}
.plan.gold li::before{border-color:#fff;background:radial-gradient(circle,#fff 2px,transparent 2.5px)}
.plan .btn{left:42px;top:476px;width:166px;height:36px}
.plan.gold .btn{background:#fff;color:var(--purple)}

.cta{left:174px;top:3212px;width:886px;height:216px;border-radius:10px;background:linear-gradient(90deg,#6a12d6,#4a3de6 60%,#3f5ae8)}
.cta h2{position:absolute;left:74px;top:62px;font-size:30px;line-height:34px;font-weight:600}
.cta p{position:absolute;left:74px;top:148px;font-size:12px}
.cta .btn{left:636px;top:118px;width:158px;height:40px;background:#fff;color:var(--blue);border-radius:20px;font-size:13px}

.quote{width:434px;height:262px;border:1.5px solid var(--line);border-radius:12px;padding:26px 28px}
.quote h5{font-size:15px;font-style:italic;font-weight:500;line-height:25px}
.quote p{font-size:10px;line-height:18px;color:var(--muted);margin-top:18px}
.person{position:absolute;left:28px;top:180px;display:flex;align-items:center;gap:22px;font-size:12px}
.avatar{width:58px;height:58px;border-radius:50%;background:linear-gradient(#e6e6ea,#9a9aa5)}
.person b{font-weight:500}
.person span{color:var(--muted)}
.arrow-btn{width:26px;height:26px;border:1.5px solid #fff;border-radius:50%;display:flex;align-items:center;justify-content:center}

.contact{left:104px;top:4043px;width:482px;height:550px;border:1.5px solid var(--line);border-radius:20px;padding:50px 44px}
.contact h2{font-size:32px;font-weight:500}
.contact .intro{font-size:11px;line-height:17px;color:var(--muted);margin-top:16px}
.field{border:1px solid #cfcbe0;border-radius:3px;height:54px;margin-top:14px;padding:16px 16px;font-size:11px;color:#ddd}
.field.tall{height:180px}
.contact .btn{position:relative;margin-top:30px;width:164px;height:46px;font-size:16px;font-weight:600;border-radius:23px}

.faq-title{left:658px;top:4136px;font-size:26px;font-weight:600;letter-spacing:.2px}
.faq{left:658px;width:432px;border:1.5px solid #cfcbe0;border-radius:6px;padding:0 20px;font-size:10px}
.faq .q{display:flex;justify-content:space-between;align-items:center;height:44px}
.faq .dot{width:20px;height:20px;border-radius:50%;background:var(--orange);display:flex;align-items:center;justify-content:center;font-size:12px}
.faq .dot.grey{background:#bdbdc6}
.faq .a{font-size:9px;line-height:15px;color:var(--muted);padding-bottom:12px}

.footer-line{left:0;top:4760px;width:1200px;height:1px;background:rgba(255,255,255,.25)}
.foot-text{left:66px;top:4900px;width:240px;font-size:10px;line-height:17px;color:var(--muted)}
.foot-links{left:416px;top:4920px;font-size:12px}
.foot-links h6{font-size:13px;font-weight:500;margin-bottom:12px}
.foot-links div{color:var(--muted);height:28px}
.vsep{width:1px;height:96px;background:rgba(255,255,255,.35)}
.social{left:652px;top:4970px;font-size:13px;font-weight:500;line-height:17px}
.social-dots{left:652px;top:5022px;display:flex;gap:20px}
.social-dots i{width:24px;height:24px;border-radius:50%;background:#fff;display:block}
.contact-list{left:900px;top:4936px;font-size:12px}
.contact-list div{display:flex;align-items:center;gap:26px;height:43px}
.bottom{top:5104px;font-size:10px;color:var(--muted)}
</style>
</head>
<body>

<div class="abs brand" style="left:66px;top:28px"><span class="brand-mark"></span>Vandrimoss</div>
<nav class="abs nav-links"><span>Features</span><span>Integrations</span><span>Why Us</span><span>More</span></nav>
<div class="abs flag"></div>
<svg class="abs" style="left:1002px;top:43px" width="10" height="8"><path d="M1 2l4 4 4-4" stroke="#fff" fill="none" stroke-width="1.5"/></svg>
<div class="btn nav-cta">Get Started</div>

<h1 class="abs center hero-title">Making cost control easy</h1>
<p class="abs hero-sub" style="text-align:center">A simple and easy-to-use purchase order system. Helping businesses gain real-time control of commitments and spend.</p>
<div class="btn btn-orange" style="left:372px;top:380px;width:162px;height:42px">Start Free Trail <span class="circle-arrow">›</span></div>
<div class="btn btn-outline" style="left:608px;top:380px;width:162px;height:42px">Book a Demo</div>
<div class="abs hero-note">*No credit card required</div>
<div class="abs hero-visual" role="img" aria-label="Vandrimoss dashboard shown on a desktop monitor, a laptop and a phone"></div>

<h2 class="abs center h2" style="top:896px">Key features in Vandrimoss</h2>

<div class="abs feature" style="left:66px;top:988px">
  <div class="icon"><svg width="30" height="30" viewBox="0 0 30 30" fill="none" stroke="#fff" stroke-width="2"><rect x="5" y="3" width="18" height="23" rx="2"/><path d="M9 9h10M9 14h10M9 19h5"/><circle cx="22" cy="23" r="4" fill="#0c0a1c"/></svg></div>
  <h3>Purchase Planning</h3>
  <p>From purchase planning to actual commitments — all-in-one system</p>
  <div class="more">learn More ⟶</div>
</div>
<div class="abs feature" style="left:338px;top:988px">
  <div class="icon"><svg width="30" height="30" viewBox="0 0 30 30" fill="none" stroke="#fff" stroke-width="2"><rect x="4" y="5" width="22" height="20" rx="2"/><path d="M9 11h12M9 15h12M9 19h12"/></svg></div>
  <h3>Purchase Order</h3>
  <p>An efficient workflow that will save time and ensure clear agreements with your supplier</p>
  <div class="more">learn More ⟶</div>
</div>
<div class="abs feature" style="left:608px;top:988px">
  <div class="icon"><svg width="30" height="30" viewBox="0 0 30 30" fill="none" stroke="#fff" stroke-width="2"><path d="M5 9l3 3 5-5M5 20l3 3 5-5M16 10h10M16 21h10"/></svg></div>
  <h3>Flexibal Approval Flow</h3>
  <p>Approve from anywhere with a flexible digital approval flow</p>
  <div class="more">learn More ⟶</div>
</div>
<div class="abs feature" style="left:880px;top:988px">
  <div class="icon"><svg width="30" height="30" viewBox="0 0 30 30" fill="none" stroke="#fff" stroke-width="2.4"><path d="M5 26h20M9 22v-6M13 22v-10M17 22v-8M21 22v-12"/></svg></div>
  <h3>Real-Time tracking</h3>
  <p>Real-time information takes away uncertainties when making important procurement decisions</p>
  <div class="more">learn More ⟶</div>
</div>
<div class="btn btn-outline" style="left:520px;top:1286px;width:162px;height:40px">See More Features</div>

<h2 class="abs int-title">Integrate seamlessly with your accounting system</h2>
<div class="abs int-text">
  <p>From purchase planning to actual commitments — all-in-one system</p>
  <p style="margin-top:12px">Connect these two powerful systems for total control of company spend and commitments. Save time spent on manual tasks and avoid unwanted budget overspending.</p>
</div>
<div class="btn btn-orange" style="left:156px;top:1650px;width:164px;height:40px">Start Free Trail <span class="circle-arrow">›</span></div>
<div class="abs int-visual" role="img" aria-label="Illustration of accounting partner connections around a business professional holding a tablet"></div>

<div class="abs center eyebrow" style="top:1804px">HOW WE DO</div>
<h2 class="abs center" style="top:1838px;font-size:30px;font-weight:600">Get Started In 1-2-3</h2>
<div class="abs" style="left:560px;top:1902px;width:80px;height:2px;background:#fff"></div>

<svg class="abs" style="left:80px;top:1925px" width="1040" height="350" fill="none" stroke="#fff" stroke-width="1.5">
  <path d="M8 180 A170 170 0 0 1 348 180"/>
  <path d="M350 180 A170 170 0 0 0 690 180"/>
  <path d="M692 180 A170 170 0 0 1 1032 180"/>
  <circle cx="8" cy="180" r="3.5" fill="#fff"/>
  <circle cx="1032" cy="180" r="3.5" fill="#fff"/>
</svg>

<div class="abs step" style="left:124px;top:1994px">
  <div class="badge"><svg width="36" height="36" viewBox="0 0 36 36" fill="none" stroke="#4b57d6" stroke-width="2"><rect x="8" y="5" width="20" height="26" rx="2"/><path d="M12 12h2M17 12h7M12 18h2M17 18h7M12 24h2M17 24h7"/></svg></div>
  <h4>Create Account</h4>
  <p>Super Easy Setup. Your Account Is Ready To Use In Less Than 5 Minutes.</p>
</div>
<div class="abs step" style="left:464px;top:1994px">
  <div class="badge"><svg width="36" height="36" viewBox="0 0 36 36" fill="none" stroke="#4b57d6" stroke-width="2"><path d="M9 4h13l6 6v22H9z"/><path d="M13 15h11M13 20h11M13 25h8"/></svg></div>
  <h4>Set Up Budget</h4>
  <p>Set Up A Budget With Desired Cost Breakdown And Set Of Approvers.</p>
</div>
<div class="abs step" style="left:804px;top:1994px">
  <div class="badge"><svg width="36" height="36" viewBox="0 0 36 36" fill="none" stroke="#e0712b" stroke-width="2"><rect x="5" y="7" width="26" height="20" rx="2"/><path d="M10 22v-5M15 22v-9M20 22v-6"/><circle cx="26" cy="17" r="3"/></svg></div>
  <h4>Create A Purchase Order</h4>
  <p>Create Your First Purchase Order And Send To Supplier. Track Budget Spend In Real-Time.</p>
</div>

<h2 class="abs center" style="top:2400px;font-size:30px;font-weight:600">Our Packages</h2>
<p class="abs center" style="top:2458px;font-size:10px;line-height:17px;color:var(--muted)">No Start-Up Cost Or Hidden Surprises. Prices Are Based On Yearly License.<br>We Can Also Offer Monthly Payments For An Extra 10% Charge On Prices Below.</p>

<div class="abs plan" style="left:66px;top:2530px">
  <div class="name">Basic</div>
  <div class="price">USD 159 <small>/ Month</small></div>
  <div class="trial">14 Day Free Trial</div>
  <ul><li>1-5 Users</li><li>Budget Module</li><li>Approval Flow</li><li>Full Support</li><li>Unlimited POs</li><li>Integration</li></ul>
  <div class="btn btn-orange">Start Free Trail <span class="circle-arrow">›</span></div>
</div>
<div class="abs plan" style="left:338px;top:2530px">
  <div class="name">Plus</div>
  <div class="price">USD 269<small>/ Month</small></div>
  <div class="trial">14 Day Free Trial</div>
  <ul><li>6-10 Users</li><li>Budget Module</li><li>Approval Flow</li><li>Full Support</li><li>Unlimited POs</li><li>Integration</li><li>Multi-Company</li><li>Planned Purchases</li><li>Cash Flow Forecast</li></ul>
  <div class="btn btn-orange">Start Free Trail <span class="circle-arrow">›</span></div>
</div>
<div class="abs plan gold" style="left:608px;top:2530px">
  <div class="name">Gold</div>
  <div class="price">USD 399<small>/ Month</small></div>
  <div class="trial" style="color:#e3d2ff">14 Day Free Trial</div>
  <ul><li>11-20 Users</li><li>Budget Module</li><li>Approval Flow</li><li>Full Support</li><li>Unlimited POs</li><li>Integration</li><li>Multi-Company</li><li>Planned Purchases</li><li>Cash Flow Forecast</li></ul>
  <div class="btn">Start Free Trail <span class="circle-arrow">›</span></div>
</div>
<div class="abs plan" style="left:880px;top:2530px">
  <div class="name">Diamond</div>
  <div class="price">USD 669<small>/ Month</small></div>
  <div class="trial">14 Day Free Trial</div>
  <ul><li>21-50 Users</li><li>Budget Module</li><li>Approval Flow</li><li>Full Support</li><li>Unlimited POs</li><li>Integration</li><li>Multi-Company</li><li>Planned Purchases</li><li>Cash Flow Forecast</li><li>API Access</li></ul>
  <div class="btn btn-orange">Start Free Trail <span class="circle-arrow">›</span></div>
</div>

<section class="abs cta">
  <h2>Simplify and professionalize your<br>procurement process today</h2>
  <p>Lorem Ipsum is simply dummy text of the printing and typesetting industry</p>
  <div class="btn">Book Demo</div>
</section>

<h2 class="abs center" style="top:3530px;font-size:28px;font-weight:600">What Our Customers Say</h2>
<div class="abs arrow-btn" style="left:70px;top:3740px"><svg width="12" height="10"><path d="M11 5H2M5 1L1 5l4 4" stroke="#fff" fill="none" stroke-width="1.5"/></svg></div>
<div class="abs arrow-btn" style="left:1104px;top:3740px"><svg width="12" height="10"><path d="M1 5h9M7 1l4 4-4 4" stroke="#fff" fill="none" stroke-width="1.5"/></svg></div>

<div class="abs quote" style="left:156px;top:3618px">
  <h5>Vandrimoss Is My New Best Friend!</h5>
  <p>Fantastic. The Support Team Is Exactly That, A Team That Supports You!<br>OCR Invoice Importing That Improves Over Time. This Has Stream Lined The Matching Process And Made Input Into Our Ledger Effortless.</p>
  <div class="person"><div class="avatar" role="img" aria-label="Portrait of Henrik L."></div><div><b>Henrik L.</b><br><span>Financial Controller, Consumer Goods</span></div></div>
</div>
<div class="abs quote" style="left:608px;top:3618px">
  <h5>Delivered Exactly What We Required – Recommend!</h5>
  <p>Very Smooth And Easy To Use For Our Business Expansion Project. VM Ensured We Hit Our Budget (Versus Prior Expansions Which Have Ran Over Budget) So The System Helped Us Achieve Our Goal. Thank You</p>
  <div class="person"><div class="avatar" role="img" aria-label="Portrait of Marcus T."></div><div><b>Marcus T.</b><br><span>CFO, Hospitality &amp; Event</span></div></div>
</div>

<section class="abs contact">
  <h2>Contact Us</h2>
  <p class="intro">Anything you want to ask us? We are here to help you.<br>Our contact details:</p>
  <div class="field">First Name</div>
  <div class="field">Email Add</div>
  <div class="field tall">Message</div>
  <div class="btn btn-orange">Submit</div>
</section>

<div class="abs eyebrow" style="left:658px;top:4112px;font-size:10px">FAQS</div>
<h2 class="abs faq-title">Frequently asked questions . . .</h2>
<div class="abs faq" style="top:4212px">
  <div class="q"><span>Is Vandrimoss easy to use, even for non-technical users?</span><span class="dot grey">–</span></div>
  <div class="a">Vandrimoss stands out as an intuitive and remarkably user-friendly system. Each user is assigned a specific role, ensuring that they are presented only with the functions relevant to their needs.</div>
</div>
<div class="abs faq" style="top:4378px"><div class="q"><span>How long does it take to implement Vandrimoss?</span><span class="dot">+</span></div></div>
<div class="abs faq" style="top:4436px"><div class="q"><span>Does Vandrimoss cover the full Purchase-To-Pay process?</span><span class="dot">+</span></div></div>
<div class="btn btn-outline" style="left:658px;top:4510px;width:168px;height:40px;font-size:14px;font-weight:600">View More FAQs</div>

<div class="abs footer-line"></div>
<div class="abs brand" style="left:66px;top:4830px;font-size:34px"><span class="brand-mark" style="width:40px;height:40px"></span>Vandrimoss</div>
<p class="abs foot-text">Lorem Ipsum is simply dummy text of the printing and typesetting industry. Lorem Ipsum has been the industry's standard dummy text</p>
<div class="btn btn-orange" style="left:66px;top:5016px;width:116px;height:30px;font-size:10px">Get Started</div>

<div class="abs foot-links"><h6>Quick Link</h6><div>Home</div><div>Features</div><div>Integrations</div><div>Pricing</div><div>Blogs</div></div>
<div class="abs vsep" style="left:600px;top:4960px"></div>
<div class="abs social">Follow Us<br>On Social Media</div>
<div class="abs social-dots"><i style="background:#3b63e8"></i><i style="background:#ef4a7a"></i><i style="background:#2d7ad6"></i><i></i></div>
<div class="abs vsep" style="left:856px;top:4960px"></div>
<div class="abs contact-list">
  <div><svg width="18" height="18" viewBox="0 0 18 18" fill="none" stroke="#fff" stroke-width="1.6"><path d="M4 2l3 3-2 2c1 2 3 4 5 5l2-2 3 3-2 3C8 15 3 10 2 4z"/></svg>+1 555-014-2290</div>
  <div><svg width="18" height="14" viewBox="0 0 18 14" fill="none" stroke="#fff" stroke-width="1.6"><rect x="1" y="1" width="16" height="12" rx="1"/><path d="M1 2l8 6 8-6"/></svg>hello@vandrimoss.example</div>
  <div><svg width="18" height="20" viewBox="0 0 18 20" fill="#fff"><path d="M9 1a7 7 0 0 0-7 7c0 5 7 11 7 11s7-6 7-11a7 7 0 0 0-7-7zm0 10a3 3 0 1 1 0-6 3 3 0 0 1 0 6z"/></svg>88 Alder Row, Millbrook 20417</div>
</div>

<div class="abs bottom" style="left:82px">© Company- All Rights Reserved</div>
<div class="abs bottom" style="left:818px">Terms and Conditions</div>
<div class="abs bottom" style="left:964px">Privacy Policy</div>
<div class="abs bottom" style="left:1060px">Disclaimer</div>

</body>
</html>
```